Please design banner ad for new website to promote .love domain names - 940x300 -for wide viewership

We are looking to create several different banners on the different ways a .love domain name can be used by new websites.

Examples of other similar top level domains (TLDs) and their banners can be found at www.orb.club and www.pim.ink.

The graphics need to be clean, crisp and readable. They can be romantic depending on their use case, but not necessary.

Potential themes to consider:
a. Dating/matchmarker domains for example tandemsky.love or plume.love
b. A couples love story in how they met i.e. NoraandTobias.love
c. Wedding website – GardenParties.love
d. Enjoyment or attachment of a hobby or object - i.e. love of cooking, enjoyment of wine, fan of a baseball club, love of tennis, etc.
e. Literature – music, poems, love stories

Dimensions of the banners should be approx. 940x300 px

Red is okay but where appropriate please use other colours other than Red.

We have a beta website http://trymarkzone.domains/ and a couple of rough examples of banners (just as demos). We want professionally designed banners that focuses either on (a) one of the what is .love themes listed in the columns on the beta site OR (b) a banner that communicates that broad and universal nature of .love (we like to remind people/consumers that .love is a good TLD for a wide range of websites from "wedding RSVP websites" - to - "sports fan club").

Target Market(s)

New domain name purchasers, new and existing businesses owners, couples who are getting married, wedding planners, stores, people who enjoy a hobby or sport and want to create a website to reflect their interests

Industry/Entity Type

Club

Requirements
Must have
• Clear, concise message that reflects the benefit of owning a .love domain name
Nice to have
• Original ideas on the use of .love on the Internet
Should not have
• Reference to Valentine's Day

```html
<!DOCTYPE html>
<html lang="en">
<head>
<meta charset="UTF-8">
<title>shorelinedays.love banner</title>
<link rel="stylesheet" href="https://fonts.googleapis.com/css2?family=Roboto+Condensed:wght@500;700&display=swap">
<style>
  :root {
    --sun-top: #e9b95a;
    --sun-mid: #f6d774;
    --sun-low: #f9e497;
    --sun-sand: #eed27c;
    --sea-deep: #1f9fa6;
    --sea-mid: #3cc0bd;
    --sea-shallow: #7fd7c6;
    --sand-light: #efe5a6;
    --foam: #f4f0c8;
    --ink: #0a0a0a;
  }
  * { margin: 0; padding: 0; box-sizing: border-box; }
  html, body { width: 1200px; height: 383px; overflow: hidden; background: #ffffff; }
  .banner { position: relative; width: 1200px; height: 383px; overflow: hidden; }
  .scene { position: absolute; top: 0; height: 383px; }
  .scene--sunset {
    left: 0; width: 544px;
    background:
      radial-gradient(ellipse 60% 35% at 45% 52%, rgba(255,248,200,0.7), rgba(255,248,200,0) 70%),
      linear-gradient(180deg, var(--sun-top) 0%, var(--sun-mid) 30%, var(--sun-low) 55%, var(--sun-sand) 100%);
  }
  .scene--shore {
    left: 544px; width: 656px;
    background:
      linear-gradient(160deg, rgba(239,229,166,0) 55%, rgba(239,229,166,0.85) 78%, var(--sand-light) 100%),
      linear-gradient(180deg, var(--sea-deep) 0%, var(--sea-mid) 40%, var(--sea-shallow) 65%, var(--foam) 100%);
  }
  .line {
    position: absolute;
    top: 106px;
    font-family: "Roboto Condensed", "Arial Narrow", sans-serif;
    font-weight: 500;
    font-size: 40px;
    line-height: 1;
    letter-spacing: 0.3px;
    color: var(--ink);
    white-space: nowrap;
  }
  .line--gave { left: 56px; }
  .line--received { left: 573px; }
  .domain {
    position: absolute;
    left: 171px;
    top: 139px;
    font-family: "Roboto Condensed", "Arial Narrow", sans-serif;
    font-weight: 700;
    font-size: 96px;
    line-height: 1;
    letter-spacing: 2px;
    color: var(--ink);
    white-space: nowrap;
  }
</style>
</head>
<body>
  <div class="banner">
    <div class="scene scene--sunset" role="img" aria-label="Golden sunset over a beach with a woman walking along the shore"></div>
    <div class="scene scene--shore" role="img" aria-label="Turquoise sea with a gentle wave rolling onto the sand"></div>
    <p class="line line--gave">I gave him the ocean</p>
    <p class="line line--received">He gave me footprints in the sand.</p>
    <h1 class="domain">shorelinedays.love</h1>
  </div>
</body>
</html>
```